Billboard design - consider what a billboard is

Design a billboard using my logo - Billboard is 6m x 3m
A Billboard is advertising for my company that is on a big sign.

Has to be clean and easy to read, and ideally highlights that we are Residential and Commercial builders.

Keep it clean and easy to read

The contact number for the board is

022 583 7092
www.harbourframeworks.co.nz
info@harbourframeworks.co.nz

Doesnt have to have all contact details if it doesnt fit

Has to catch peoples attention to contact us if they need a builder

Can you please change the sign to be all white writing, with black background ?
Updates

Please consider what a billboard is...

The design needs to be suitable for a billboard..

Target Market(s)

people driving past

Industry/Entity Type

Construction

Logo Text

Wellington Builder, website email address, contact number

Colors
0054AA
0677BA
7BADD7
CADEEF
E8F1F8

Requirements
Must have
• Easy to read
Nice to have
• easy to read, can clearly see contact details

```html
<!DOCTYPE html>
<html lang="en">
<head>
<meta charset="utf-8">
<title>Harbour Frameworks – Billboard</title>
<link rel="stylesheet" href="https://fonts.googleapis.com/css2?family=Michroma&family=Poppins:wght@400;500;600;800&display=swap">
<style>
  :root {
    --page: #ffffff;
    --panel-white: #ffffff;
    --night: #0f1620;
    --sky-blue: #4f93e6;
    --brand-blue: #4b84c6;
    --taupe: #6f6462;
    --text-white: #ffffff;
  }
  html, body {
    margin: 0;
    padding: 0;
    width: 892px;
    height: 1200px;
    overflow: hidden;
    background: var(--page);
  }
  .canvas {
    position: relative;
    width: 892px;
    height: 1200px;
  }
  .billboard {
    position: absolute;
    left: 46px;
    top: 400px;
    width: 800px;
    height: 400px;
    box-shadow: 0 6px 22px rgba(0, 0, 0, 0.28);
  }
  .billboard svg { display: block; width: 100%; height: 100%; }
  .fill-white { fill: var(--panel-white); }
  .fill-night { fill: var(--night); }
  .fill-blue { fill: var(--sky-blue); }
  .fill-taupe { fill: var(--taupe); }
  .brand-mark { fill: var(--taupe); }
  .brand-name {
    font-family: "Poppins", sans-serif;
    font-weight: 600;
    fill: var(--brand-blue);
  }
  .intro {
    font-family: "Poppins", sans-serif;
    font-weight: 500;
    font-size: 72px;
    fill: var(--text-white);
  }
  .headline {
    font-family: "Poppins", sans-serif;
    font-weight: 800;
    font-size: 90px;
    fill: var(--sky-blue);
  }
  .headline-amp {
    font-family: "Poppins", sans-serif;
    font-weight: 500;
    font-size: 86px;
    fill: var(--text-white);
  }
  .trade {
    font-family: "Poppins", sans-serif;
    font-weight: 400;
    font-size: 46px;
    letter-spacing: 17px;
    fill: var(--text-white);
  }
  .phone {
    font-family: "Michroma", sans-serif;
    font-size: 60px;
    fill: var(--text-white);
  }
  .contact {
    font-family: "Poppins", sans-serif;
    font-weight: 500;
    font-size: 34px;
    fill: var(--text-white);
  }
</style>
</head>
<body>
<main class="canvas">
  <section class="billboard" aria-label="Harbour Frameworks billboard">
    <svg viewBox="0 0 1265 632" xmlns="http://www.w3.org/2000/svg">
      <!-- panels -->
      <rect class="fill-white" x="0" y="0" width="1265" height="632"/>
      <polygon class="fill-blue" points="312,0 1265,0 1265,632 312,632 497,340"/>
      <polygon class="fill-night" points="344,0 1265,0 1265,632 340,632 527,340"/>
      <polygon class="fill-white" points="529,345 1265,345 1265,352 534,352"/>
      <polygon class="fill-taupe" points="534,352 1265,352 1265,632 362,632"/>
      <polygon class="fill-blue" points="455,382 1204,382 1204,466 398,466"/>

      <!-- brand -->
      <g class="brand">
        <rect class="brand-mark" x="62" y="262" width="34" height="34"/>
        <text class="brand-name" x="110" y="294" font-size="50" textLength="190" lengthAdjust="spacingAndGlyphs">Harbour</text>
        <text class="brand-name" x="62" y="340" font-size="30" textLength="238" lengthAdjust="spacingAndGlyphs">FRAMEWORKS</text>
      </g>

      <!-- message -->
      <text class="intro" x="567" y="103">we are</text>
      <text class="headline" x="567" y="183" textLength="545" lengthAdjust="spacingAndGlyphs">RESIDENTIAL</text>
      <text class="headline-amp" x="1133" y="183">&amp;</text>
      <text class="headline" x="567" y="255" textLength="602" lengthAdjust="spacingAndGlyphs">COMMERCIAL</text>
      <text class="trade" x="577" y="313">BUILDERS</text>

      <!-- contact -->
      <text class="phone" x="522" y="446" textLength="640" lengthAdjust="spacingAndGlyphs">022 583 7092</text>
      <text class="contact" x="522" y="520" textLength="632" lengthAdjust="spacingAndGlyphs">info@harbourframeworks.co.nz</text>
      <text class="contact" x="524" y="573" textLength="630" lengthAdjust="spacingAndGlyphs">www.harbourframeworks.co.nz</text>
    </svg>
  </section>
</main>
</body>
</html>
```